Trailer Wrap "Copper Ridge Bullion Traders"

The assignment is to design a “Wrap” for a trailer that we will use as a mobile office to buy gold.
Want to make the trailer a Very HARD CORE “Billboard”
When you see it – You Understand what we do
When you see it – You want to bring us your gold
Details - Copper Ridge Bullion Traders will be buying a trailer to pull behind a truck that will be used as a mobile office to buy Gold from consumers.
The Trailer
The trailer needs to serve as a “Billboard” for the gold buying business.
We will be pulling the trailer up to retail stores and parking it in the parking lot a few days prior to buying gold
Gold
We will be buying gold jewelry including rings, bracelets, chains, coins etc.
Anything that has gold in it
The Trailer
Trailer is:
2o feet long and 7 feet high
The end of the Trailer is 8 long and 7 feet high
We will want to wrap both sides and ends
Copy
We Buy Gold
Cash On the Spot
Buying all Gold jewelry – Rings, Bracelets, Chains, Coins
Convert you Jewelry into Cash Today
Show Gold Bars, Rings Chains Coin and Hand with CASH and hundred dollar bills
Updates
Please add the Copper Ridge Bullion Traders Logo to all designs.
We have one Great design so far....
THANKS!!!
DEREK
THANKS!!!
DEREK
Requirements
Must have
- MUST BE A HARD CORE DESIGN -
- When you see it – You Understand what we do
- When you see it – You want to bring us your gold
Copy
- We Buy Gold
- Cash On the Spot
- Buying all Gold jewelry – Rings, Bracelets, Chains, Coins
- Convert you Jewelry into Cash Today
- Show Gold Bars, Rings Chains Coin and Hand with CASH and hundred dollar bills
- Name of Company "Copper Ridge Bullion Traders"

```html
<!DOCTYPE html>
<html lang="en">
<head>
<meta charset="utf-8">
<title>Copper Ridge Bullion Traders – Trailer Wrap</title>
<link href="https://fonts.googleapis.com/css2?family=Archivo+Black&family=Cinzel:wght@900&family=Open+Sans:ital,wght@1,800&display=swap" rel="stylesheet">
<style>
  :root {
    --fire-deep: #7a0c05;
    --fire-mid: #e0440e;
    --fire-glow: #ffb21e;
    --gold: #e8b437;
    --bill-light: #e6e4c8;
    --bill-mid: #b9c19a;
    --bill-dark: #5e6b48;
    --headline-blue: #1a4ea3;
    --cash-red: #d4121b;
    --white: #ffffff;
    --list-gold: #c8b23a;
    --list-edge: #3b3a12;
  }
  * { margin: 0; padding: 0; box-sizing: border-box; }
  html, body { width: 1200px; height: 420px; overflow: hidden; background: #ffffff; }
  .wrap {
    position: relative;
    width: 1200px;
    height: 420px;
    overflow: hidden;
  }
  .art { position: absolute; inset: 0; }
  .headline {
    position: absolute;
    left: 22px;
    top: 8px;
    font-family: "Archivo Black", sans-serif;
    font-size: 70px;
    line-height: 1;
    letter-spacing: 1px;
    color: var(--white);
    -webkit-text-stroke: 3px var(--headline-blue);
    paint-order: stroke fill;
    text-shadow: 3px 4px 0 rgba(0,0,0,0.35);
  }
  .cash-banner {
    position: absolute;
    left: 0;
    top: 108px;
    width: 470px;
    height: 82px;
    background: linear-gradient(90deg, var(--white) 75%, rgba(255,255,255,0));
  }
  .cash-line {
    position: absolute;
    left: 60px;
    top: 112px;
    font-family: "Archivo Black", sans-serif;
    font-size: 58px;
    line-height: 1.2;
    color: var(--cash-red);
  }
  .buying-line {
    position: absolute;
    left: 440px;
    top: 206px;
    text-align: center;
    font-family: "Archivo Black", sans-serif;
    font-size: 31px;
    line-height: 1.15;
    color: var(--white);
    -webkit-text-stroke: 2px var(--headline-blue);
    paint-order: stroke fill;
  }
  .brand {
    position: absolute;
    left: 14px;
    top: 268px;
    width: 130px;
    display: flex;
    flex-direction: column;
    align-items: center;
    gap: 8px;
  }
  .brand-dot {
    width: 84px;
    height: 84px;
    border-radius: 50%;
    background: var(--white);
  }
  .brand-name {
    font-family: "Archivo Black", sans-serif;
    font-size: 12px;
    line-height: 1.15;
    text-align: center;
    color: var(--white);
  }
  .item-list {
    position: absolute;
    left: 818px;
    top: 110px;
    list-style: none;
    font-family: "Cinzel", serif;
    font-weight: 900;
    font-size: 44px;
    line-height: 52px;
    color: var(--list-gold);
    -webkit-text-stroke: 2px var(--list-edge);
    paint-order: stroke fill;
  }
  .cta {
    position: absolute;
    right: 14px;
    bottom: 16px;
    font-family: "Open Sans", sans-serif;
    font-style: italic;
    font-weight: 800;
    font-size: 21px;
    color: var(--white);
    text-shadow: 1px 1px 2px rgba(0,0,0,0.6);
  }
</style>
</head>
<body>
<main class="wrap">
  <svg class="art" width="1200" height="420" viewBox="0 0 1200 420" aria-hidden="false">
    <defs>
      <radialGradient id="fire" cx="0.35" cy="0.4" r="0.8">
        <stop offset="0" stop-color="var(--fire-glow)"/>
        <stop offset="0.45" stop-color="var(--fire-mid)"/>
        <stop offset="1" stop-color="var(--fire-deep)"/>
      </radialGradient>
      <linearGradient id="bill" x1="0" y1="0" x2="1" y2="1">
        <stop offset="0" stop-color="var(--bill-light)"/>
        <stop offset="0.6" stop-color="var(--bill-mid)"/>
        <stop offset="1" stop-color="var(--bill-dark)"/>
      </linearGradient>
    </defs>
    <rect width="1200" height="420" fill="url(#fire)" role="img" aria-label="Photo of flames with gold coins, gold bars and hundred dollar bills"/>
    <polygon points="640,0 1200,0 1200,420 450,420" fill="url(#bill)" role="img" aria-label="Illustration of an oversized hundred dollar bill"/>
    <rect x="450" y="370" width="750" height="50" fill="var(--bill-dark)" opacity="0.55"/>
  </svg>

  <h1 class="headline">WE BUY GOLD</h1>
  <div class="cash-banner"></div>
  <p class="cash-line">Ca$h on the Spot</p>
  <p class="buying-line">Buying all<br>Gold jewelry</p>

  <div class="brand">
    <span class="brand-dot"></span>
    <span class="brand-name">COPPER RIDGE BULLION TRADERS</span>
  </div>

  <ul class="item-list">
    <li>RINGS</li>
    <li>BRACELETS</li>
    <li>CHAINS</li>
    <li>COINS</li>
  </ul>

  <p class="cta">Convert you Jewelry into Cash Today!!!</p>
</main>
</body>
</html>
```